Yard sign

Looking for a yard sign. <br/>Something simple, name, number. <br/>Large text, readable from 50 feet away. <br/><br/>18 x 24 inches.

Target Market(s)

Potential homeowners thinking about going solar.

Colors

Designer to choose colors to be used in the design.

Requirements
Must have
• "WE'VE GONE SOLAR!"
Nice to have
• We are a solar company, we would like a design that compliments the homeowners decision that they went solar and encourages others to do the same.

```html
<!DOCTYPE html>
<html lang="en">
<head>
<meta charset="utf-8">
<title>Suncrest Yard Signs</title>
<link rel="stylesheet" href="https://fonts.googleapis.com/css2?family=League+Spartan:wght@400;600;700&display=swap">
<style>
  :root {
    --page: #ffffff;
    --photo-dark: #24142c;
    --photo-mid: #3a2743;
    --photo-light: #4c3a55;
    --night: #04021a;
    --white: #ffffff;
    --brand-orange: #f28c28;
    --brand-gold: #f5c12a;
    --band-light: #dd8a2e;
    --band-dark: #d07a22;
  }
  * { margin: 0; padding: 0; box-sizing: border-box; }
  html, body {
    width: 1200px;
    height: 816px;
    overflow: hidden;
    background: var(--page);
    font-family: "League Spartan", "Helvetica Neue", Arial, sans-serif;
  }
  .canvas { position: relative; width: 1200px; height: 816px; }
  .sign {
    position: absolute;
    top: 53px;
    width: 531px;
    height: 708px;
    overflow: hidden;
    box-shadow: 0 8px 30px rgba(0, 0, 0, 0.22);
  }
  .sign--photo { left: 53px; }
  .sign--night { left: 615px; background: var(--night); }
  .sign__photo {
    position: absolute;
    inset: 0;
    background:
      radial-gradient(ellipse at 60% 60%, var(--photo-light) 0%, transparent 55%),
      linear-gradient(160deg, var(--photo-dark) 0%, var(--photo-mid) 45%, var(--photo-dark) 100%);
  }
  .headline {
    position: absolute;
    color: var(--white);
    font-weight: 700;
  }
  .sign--photo .headline {
    left: 66px;
    top: 66px;
    font-size: 46px;
    line-height: 57px;
    letter-spacing: 0.04em;
  }
  .sign--night .headline {
    left: 79px;
    top: 54px;
    font-size: 47px;
    line-height: 61px;
    font-weight: 600;
    letter-spacing: 0.12em;
  }
  .headline__accent {
    display: block;
    font-size: 61px;
    font-weight: 700;
    line-height: 56px;
    letter-spacing: 0.1em;
  }
  .brand {
    position: absolute;
    left: 0;
    right: 0;
    top: 362px;
    display: flex;
    align-items: center;
    justify-content: center;
    gap: 14px;
  }
  .brand__dot {
    width: 40px;
    height: 40px;
    border-radius: 50%;
    background: var(--brand-gold);
  }
  .brand__name {
    color: var(--brand-orange);
    font-size: 68px;
    font-weight: 700;
    letter-spacing: 0.02em;
    line-height: 1;
    padding-top: 8px;
  }
  .tagline {
    position: absolute;
    left: 0;
    right: 0;
    top: 502px;
    text-align: center;
    color: var(--white);
    font-size: 25px;
    font-weight: 400;
    letter-spacing: 0.1em;
  }
  .contact-band {
    position: absolute;
    left: 9px;
    right: 9px;
    top: 627px;
    height: 73px;
    display: flex;
    align-items: center;
    justify-content: center;
    color: var(--white);
    font-size: 34px;
    font-weight: 700;
    letter-spacing: 0.16em;
    padding-top: 6px;
  }
  .sign--photo .contact-band { background: var(--band-light); }
  .sign--night .contact-band { background: var(--band-dark); }
</style>
</head>
<body>
<main class="canvas">
  <section class="sign sign--photo">
    <div class="sign__photo" role="img" aria-label="Aerial photo of a house with solar panels on its roof, under a dark purple tint"></div>
    <h1 class="headline">We've<br>gone<br>solar!</h1>
    <div class="brand"><span class="brand__dot"></span><span class="brand__name">SUNCREST</span></div>
    <p class="tagline">SOLAR MADE EASY</p>
    <div class="contact-band">TEL: 555-0142-876</div>
  </section>

  <section class="sign sign--night">
    <h1 class="headline">THINKING<br>ABOUT GOING<span class="headline__accent">SOLAR?</span></h1>
    <div class="brand"><span class="brand__dot"></span><span class="brand__name">SUNCREST</span></div>
    <p class="tagline">SOLAR MADE EASY</p>
    <div class="contact-band">TEL: 555-0142-876</div>
  </section>
</main>
</body>
</html>
```